VELUNDO Brisbane Tiling Service

My name is Mirko Bostel i need a business card for a new company. We are wall and floor tilers based in Brisbane, our company is Velundio Brisbane Tiling Service.
We would like a logo from our website used on our cards. Our website is www.velundio.com.au

I would like my Facebook and Twitter accounts on my card.

Industry/Entity Type

Business

Colors
0692cd
3176b5
33a6d7
85cae6

```html
<!DOCTYPE html>
<html lang="en">
<head>
<meta charset="utf-8">
<title>Velundio Business Card</title>
<link rel="stylesheet" href="https://fonts.googleapis.com/css2?family=Source+Sans+3:wght@400;600;700&display=swap">
<style>
  :root {
    --blue-bright: #0692cd;
    --blue-deep: #3176b5;
    --blue-mid: #33a6d7;
    --blue-light: #85cae6;
    --card-border: #8a8a8a;
    --paper: #ffffff;
  }
  * { margin: 0; padding: 0; box-sizing: border-box; }
  html, body {
    width: 1012px;
    height: 1200px;
    overflow: hidden;
    background: var(--paper);
    font-family: "Source Sans 3", sans-serif;
  }
  .canvas { position: relative; width: 1012px; height: 1200px; }
  .card {
    position: absolute;
    left: 22px;
    width: 967px;
    height: 566px;
    border: 1px solid var(--card-border);
    background: var(--paper);
    overflow: hidden;
  }
  .card--front { top: 24px; }
  .card--back { top: 612px; }

  /* Front */
  .brand {
    position: absolute;
    left: 84px;
    top: 213px;
    display: flex;
    align-items: center;
    gap: 22px;
  }
  .brand__square {
    width: 150px;
    height: 150px;
    border-radius: 4px;
    background: var(--blue-mid);
  }
  .brand__text { display: flex; flex-direction: column; }
  .brand__name {
    font-size: 138px;
    font-weight: 600;
    line-height: 0.9;
    color: var(--blue-mid);
    letter-spacing: 1px;
  }
  .brand__tagline {
    margin-top: 12px;
    font-size: 27px;
    font-weight: 600;
    letter-spacing: 10.8px;
    color: var(--blue-deep);
    white-space: nowrap;
  }
  .since {
    position: absolute;
    right: 34px;
    top: 508px;
    font-size: 18px;
    color: var(--blue-deep);
  }
  .since__label { font-size: 11px; letter-spacing: 6px; }

  /* Back */
  .holder {
    position: absolute;
    left: 32px;
    top: 26px;
    font-size: 40px;
    font-weight: 600;
    color: var(--blue-deep);
  }
  .social {
    position: absolute;
    left: 32px;
    top: 89px;
    list-style: none;
  }
  .social__item {
    display: flex;
    align-items: center;
    gap: 4px;
    height: 31px;
    font-size: 19px;
    font-weight: 600;
    color: var(--blue-mid);
  }
  .social__item--secondary { color: var(--blue-deep); }
  .social__mark { width: 24px; height: 24px; background: currentColor; }
  .email {
    position: absolute;
    left: 32px;
    top: 150px;
    font-size: 31px;
    font-weight: 600;
    color: var(--blue-mid);
  }
  .details {
    position: absolute;
    left: 32px;
    top: 362px;
    list-style: none;
  }
  .details__row {
    height: 44px;
    font-size: 33px;
    font-weight: 600;
    color: var(--blue-mid);
    line-height: 44px;
  }
  .back-mark {
    position: absolute;
    right: 20px;
    top: 372px;
    font-size: 82px;
    font-weight: 600;
    line-height: 1;
    color: var(--blue-light);
  }
</style>
</head>
<body>
<main class="canvas">
  <section class="card card--front" aria-label="Card front">
    <div class="brand">
      <div class="brand__square" aria-hidden="true"></div>
      <div class="brand__text">
        <span class="brand__name">velundio</span>
        <span class="brand__tagline">WALL AND FLOOR TILING</span>
      </div>
    </div>
    <p class="since"><span class="since__label">SINCE</span> 1996</p>
  </section>

  <section class="card card--back" aria-label="Card back">
    <h1 class="holder">Mirko Bostel</h1>
    <ul class="social">
      <li class="social__item"><span class="social__mark" aria-hidden="true"></span>/Infovelundio</li>
      <li class="social__item social__item--secondary"><span class="social__mark" aria-hidden="true"></span>/velundio</li>
    </ul>
    <p class="email">Email: info@velundio.com.au</p>
    <ul class="details">
      <li class="details__row">Tel: 0400 555 218</li>
      <li class="details__row">Tel: 07 3100 4427</li>
      <li class="details__row">Abn: 51824630975</li>
      <li class="details__row">Qbcc: 1093462</li>
    </ul>
    <span class="back-mark">velundio</span>
  </section>
</main>
</body>
</html>
```